A label for my commercially sold local honey. This is a LABEL not a logo

3 inches high
2 inches wide

Target Market(s)

Customers who like "local" honey

Logo Text

Wildflower Honey -- 100% Pure & Unfiltered -- Florida

Logo styles of interest
Wordmark Logo
Requirements
Must have
• Wildflower Honey -- 100% Pure & Unfiltered -- Florida

Florida should be dominant

3 inches high / 2 inches wide

```html
<!DOCTYPE html>
<html lang="en">
<head>
<meta charset="utf-8">
<title>Wildflower Honey Label</title>
<link rel="stylesheet" href="https://fonts.googleapis.com/css2?family=Bebas+Neue&family=Oswald:wght@400;500&family=Barlow+Semi+Condensed:wght@500;600&display=swap">
<style>
  :root {
    --gold-light: #fbe96a;
    --gold: #e8b920;
    --gold-deep: #c8891a;
    --ink: #111111;
    --charcoal: #2b2b2b;
    --slate: #5a5a5a;
    --black: #050505;
  }
  * { margin: 0; padding: 0; box-sizing: border-box; }
  html, body {
    width: 800px;
    height: 1200px;
    overflow: hidden;
    background: var(--black);
  }
  .label {
    position: relative;
    width: 800px;
    height: 1200px;
    overflow: hidden;
    background: var(--charcoal);
  }
  .comb-backdrop {
    position: absolute;
    inset: 0;
    background:
      radial-gradient(ellipse at 50% 55%, rgba(232,185,32,0.18), transparent 60%),
      linear-gradient(90deg, var(--charcoal) 0%, var(--slate) 30%, #3a3a3a 55%, var(--slate) 80%, var(--charcoal) 100%);
  }
  .honey-drip {
    position: absolute;
    left: 0;
    top: 0;
    width: 800px;
    height: 340px;
    background: linear-gradient(90deg, var(--gold-deep) 0%, var(--gold-light) 35%, var(--gold) 60%, var(--gold-light) 85%, var(--gold-deep) 100%);
    border-radius: 0 0 40px 40px;
  }
  .title {
    position: absolute;
    left: 0;
    width: 800px;
    text-align: center;
    font-family: "Oswald", sans-serif;
    font-weight: 400;
    color: var(--ink);
    line-height: 1;
  }
  .title--wildflower {
    top: 128px;
    font-size: 84px;
    letter-spacing: 26px;
    padding-left: 26px;
  }
  .title--honey {
    top: 228px;
    font-size: 84px;
    letter-spacing: 26px;
    padding-left: 26px;
  }
  .purity-badge {
    position: absolute;
    left: 0;
    top: 0;
    width: 800px;
    height: 1200px;
  }
  .purity-badge__percent {
    position: absolute;
    left: 0;
    top: 548px;
    width: 800px;
    text-align: center;
    font-family: "Barlow Semi Condensed", sans-serif;
    font-weight: 500;
    font-size: 100px;
    line-height: 1;
    color: var(--ink);
  }
  .purity-badge__claim {
    position: absolute;
    left: 0;
    top: 678px;
    width: 800px;
    text-align: center;
    font-family: "Barlow Semi Condensed", sans-serif;
    font-weight: 500;
    font-size: 34px;
    line-height: 1;
    color: var(--gold);
  }
  .origin-band {
    position: absolute;
    left: 0;
    top: 862px;
    width: 800px;
    height: 262px;
    background: linear-gradient(180deg, var(--black) 0%, #3c3c3c 45%, var(--black) 100%);
    border-top: 5px solid var(--gold);
    border-bottom: 5px solid var(--gold);
  }
  .origin-band__name {
    position: absolute;
    left: 0;
    top: 18px;
    width: 800px;
    text-align: center;
    font-family: "Bebas Neue", sans-serif;
    font-size: 276px;
    line-height: 1;
    letter-spacing: 2px;
    color: var(--gold);
    background: linear-gradient(180deg, var(--gold-light) 0%, var(--gold) 50%, var(--gold-deep) 100%);
    -webkit-background-clip: text;
    background-clip: text;
    -webkit-text-fill-color: transparent;
  }
</style>
</head>
<body>
  <main class="label">
    <div class="comb-backdrop" role="img" aria-label="Dark honeycomb pattern with golden floral swirls"></div>
    <div class="honey-drip" role="img" aria-label="Golden honey dripping down from the top edge"></div>

    <h1 class="title title--wildflower">WILDFLOWER</h1>
    <h2 class="title title--honey">HONEY</h2>

    <svg class="purity-badge" viewBox="0 0 800 1200" aria-hidden="true">
      <defs>
        <linearGradient id="badgeGold" x1="0" y1="0" x2="1" y2="1">
          <stop offset="0" stop-color="#fbe96a"/>
          <stop offset="0.5" stop-color="#e8b920"/>
          <stop offset="1" stop-color="#c8891a"/>
        </linearGradient>
        <clipPath id="badgeClip">
          <polygon points="400,452 568,540 568,714 400,802 232,714 232,540"/>
        </clipPath>
      </defs>
      <polygon points="400,440 580,534 580,720 400,814 220,720 220,534" fill="#e8b920"/>
      <polygon points="400,447 573,537 573,717 400,807 227,717 227,537" fill="url(#badgeGold)" stroke="#111111" stroke-width="6"/>
      <rect x="220" y="667" width="360" height="60" fill="#050505" clip-path="url(#badgeClip)"/>
    </svg>
    <p class="purity-badge__percent">100%</p>
    <p class="purity-badge__claim">PURE &amp; UNFILTERED</p>

    <section class="origin-band">
      <p class="origin-band__name">FLORIDA</p>
    </section>
  </main>
</body>
</html>
```